Salve Label

2.25 inch round label.

We are looking for a simple label, muted natural colors, sophisticated, elegant, calming.

Name of Product: Herbal Beeswax Salve
This scent is lavender - but there will be others scents
Want this label to be adaptable to other scents with simple color and word changes.

Other things to express on the label - all natural, calming, relaxing

Name of the Company: Copper Hollow Farm
2 oz.

```html
<!DOCTYPE html>
<html lang="en">
<head>
<meta charset="utf-8">
<title>Herbal Beeswax Salve – Lavender Label</title>
<link href="https://fonts.googleapis.com/css2?family=Poiret+One&family=Josefin+Sans:wght@300;400;600&family=Kaushan+Script&display=swap" rel="stylesheet">
<style>
  :root {
    --paper: #ffffff;
    --ring: #c55e8e;
    --title: #c45d8e;
    --scent: #8a68ad;
    --scent-name: #8562ab;
    --face-light: #fbfbfb;
    --face-mid: #eeeff0;
    --face-dark: #e2e3e5;
    --ring-text: #ffffff;
  }
  html, body {
    margin: 0;
    padding: 0;
    width: 1200px;
    height: 1200px;
    overflow: hidden;
    background: var(--paper);
  }
  .canvas {
    position: relative;
    width: 1200px;
    height: 1200px;
  }
  .label {
    position: absolute;
    inset: 0;
    width: 1200px;
    height: 1200px;
  }
  .ring-text {
    font-family: "Josefin Sans", sans-serif;
    font-weight: 400;
    font-size: 22px;
    letter-spacing: 1px;
    fill: var(--ring-text);
  }
  .product-name {
    font-family: "Poiret One", sans-serif;
    font-size: 82px;
    fill: var(--title);
    text-anchor: middle;
  }
  .scent-caption {
    font-family: "Josefin Sans", sans-serif;
    font-weight: 300;
    font-size: 27px;
    letter-spacing: 3px;
    fill: var(--scent);
    text-anchor: middle;
  }
  .scent-name {
    font-family: "Kaushan Script", cursive;
    font-size: 80px;
    fill: var(--scent-name);
    text-anchor: middle;
  }
  .net-weight {
    font-family: "Josefin Sans", sans-serif;
    font-weight: 600;
    font-size: 27px;
    fill: var(--ring-text);
    text-anchor: middle;
  }
  .weight-tab { fill: var(--ring); }
</style>
</head>
<body>
<div class="canvas">
  <svg class="label" viewBox="0 0 1200 1200" xmlns="http://www.w3.org/2000/svg">
    <defs>
      <radialGradient id="face-sheen" cx="0.55" cy="0.45" r="0.65">
        <stop offset="0" stop-color="var(--face-light)"/>
        <stop offset="0.55" stop-color="var(--face-mid)"/>
        <stop offset="1" stop-color="var(--face-dark)"/>
      </radialGradient>
      <filter id="label-shadow" x="-20%" y="-20%" width="140%" height="140%">
        <feDropShadow dx="0" dy="10" stdDeviation="14" flood-color="#000" flood-opacity="0.14"/>
      </filter>
      <path id="ring-path" d="M600,274 a325,325 0 1,1 -0.01,0"/>
    </defs>

    <circle class="label-ring" cx="600" cy="599" r="350" fill="var(--ring)" filter="url(#label-shadow)"/>
    <circle class="label-face" cx="600" cy="599" r="300" fill="url(#face-sheen)"/>

    <text class="ring-text">
      <textPath href="#ring-path" textLength="2035" lengthAdjust="spacing">COPPER HOLLOW FARM   COPPER HOLLOW FARM   COPPER HOLLOW FARM   COPPER HOLLOW FARM   COPPER HOLLOW FARM   COPPER HOLLOW FARM   </textPath>
    </text>

    <text class="product-name" x="596" y="440" textLength="378" lengthAdjust="spacingAndGlyphs">HERBAL</text>
    <text class="product-name" x="599" y="516" textLength="441" lengthAdjust="spacingAndGlyphs">BEESWAX</text>
    <text class="product-name" x="600" y="594" textLength="281" lengthAdjust="spacingAndGlyphs">SALVE</text>

    <text class="scent-caption" x="584" y="665">SCENT</text>
    <text class="scent-name" x="596" y="738" textLength="300" lengthAdjust="spacingAndGlyphs">Lavender</text>

    <path class="weight-tab" d="M556,797 L652,801 Q646,818 626,828 L543,828 Q541,808 556,797 Z"/>
    <text class="net-weight" x="597" y="823">2 oz.</text>
  </svg>
</div>
</body>
</html>
```